Cards for Employees

We are looking for an Anniversary and a Birthday card to send to our employees. 2 designs.
We send these cards to our employees based on number of years they work at the company.
Check out our website for more info.
www.BrookfieldServices.example
Target Market(s)
Our Employees -
Font styles to use
Sans Serif
Colors
Designer to choose colors to be used in the design.
Requirements
Must have
- Anniversary card - appreciation for hard work and dedication
Logo - no changes

```html
<!DOCTYPE html>
<html lang="en">
<head>
<meta charset="utf-8">
<title>Save the Date – Brookfield Services</title>
<link href="https://fonts.googleapis.com/css2?family=Michroma&family=PT+Serif&family=Montserrat:wght@700&display=swap" rel="stylesheet">
<style>
  :root {
    --stage: #434142;
    --blue-top: #1b4aa3;
    --blue-mid: #1d3c8e;
    --blue-bottom: #1a2865;
    --red: #e31d2b;
    --white: #ffffff;
  }
  html, body {
    margin: 0;
    width: 1200px;
    height: 1200px;
    overflow: hidden;
    background: var(--stage);
  }
  .card {
    position: absolute;
    left: 0;
    top: 135px;
    width: 1200px;
    height: 930px;
    overflow: hidden;
    background: linear-gradient(180deg, var(--blue-top) 0%, var(--blue-mid) 50%, var(--blue-bottom) 100%);
    color: var(--white);
  }
  .brand-name {
    position: absolute;
    top: 200px;
    left: 0;
    width: 100%;
    text-align: center;
    font-family: "Montserrat", sans-serif;
    font-weight: 700;
    font-size: 54px;
    letter-spacing: 2px;
    text-transform: uppercase;
    color: var(--white);
  }
  .headline {
    position: absolute;
    top: 398px;
    left: 0;
    width: 100%;
    margin: 0;
    text-align: center;
    white-space: nowrap;
    font-family: "Michroma", sans-serif;
    font-weight: 400;
    font-size: 74px;
    letter-spacing: 4px;
    line-height: 1.1;
    text-shadow: 0 4px 8px rgba(0, 0, 0, 0.35);
  }
  .rule {
    position: absolute;
    height: 5px;
    background: var(--red);
  }
  .rule--top { top: 524px; left: 126px; width: 952px; }
  .rule--bottom { top: 651px; left: 120px; width: 952px; }
  .tagline {
    position: absolute;
    top: 558px;
    left: 0;
    width: 100%;
    margin: 0;
    text-align: center;
    white-space: nowrap;
    font-family: "PT Serif", serif;
    font-size: 38px;
    letter-spacing: 0.5px;
  }
  .detail-frame {
    position: absolute;
    top: 792px;
    left: 133px;
    width: 932px;
    height: 200px;
    border: 1.5px solid rgba(255, 255, 255, 0.85);
    box-sizing: border-box;
  }
  .date-ribbon {
    position: absolute;
    top: 752px;
    left: 383px;
    width: 440px;
    height: 84px;
  }
  .date-ribbon__text {
    position: absolute;
    top: 752px;
    left: 383px;
    width: 440px;
    height: 84px;
    line-height: 84px;
    text-align: center;
    font-family: "PT Serif", serif;
    font-size: 76px;
    color: var(--white);
  }
</style>
</head>
<body>
  <main class="card">
    <div class="brand-name">Brookfield Services</div>

    <h1 class="headline">SAVE THE DATE</h1>

    <div class="rule rule--top"></div>
    <p class="tagline">Your contributions to the company are greatly appreciated.</p>
    <div class="rule rule--bottom"></div>

    <div class="detail-frame"></div>

    <svg class="date-ribbon" viewBox="0 0 440 84" aria-hidden="true">
      <polygon points="3,2 22,2 22,82 3,82 13,42" fill="#1d3c8e" stroke="rgba(255,255,255,0.8)" stroke-width="1.2"/>
      <polygon points="437,2 418,2 418,82 437,82 427,42" fill="#1d3c8e" stroke="rgba(255,255,255,0.8)" stroke-width="1.2"/>
      <polygon points="20,2 420,2 408,42 420,82 20,82 32,42" fill="#e31d2b"/>
    </svg>
    <div class="date-ribbon__text">10.08.20</div>
  </main>
</body>
</html>
```